ROB & JO’S GOODBYE TO MIDGE BITES

I require an attractive appealing label with the dimensions 7.5m x 3.5cm
This is a Natural sandfly insect repellent cream formulated by 2 pharmacists Carla Whitby and Rob Kettering. It is required for labelling a 50 g jar

Contains Essential Oils of cedar wood, rosemary, cinnamon, citronella, lavender, eucalyptus and clove in a moisturising base.

We would like to see designs using the colour bright duck egg blue as the main colour with dark brown tones for the patterns. An eye catching label is output aim . However any colour combination that is attractive to the eye is welcome
A gloss finish is preferable.

More designs please

Target Market(s)

Trekkers, outdoor active people, pharmacy, health shops

Colors
abd037
34a6d7
0456a4
33b8a4

Requirements
Must have
• Rob and Jo’s
• Goodbye to Midge bites
• Natural Sandfly Repellent
• Contains Essential Oils of cedar wood, rosemary, cinnamon, citronella, lavender, eucalyptus and clove in a moisturising base.
• Formulated by Australian Pharmacists Carla Whitby and Rob Kettering
• Made in Australia
• 0413862207
Nice to have
• Sandfly/ flies
• I have attached a label I use for my mozzie cream and would like a similar font please

```html
<!DOCTYPE html>
<html lang="en">
<head>
<meta charset="utf-8">
<title>Rob &amp; Jo’s Goodbye to Midge Bites – Jar Label</title>
<link href="https://fonts.googleapis.com/css2?family=Kalam:wght@400;700&family=Arimo:wght@400;700&display=swap" rel="stylesheet">
<style>
  :root {
    --backdrop: #6b6b6b;
    --label-blue: #abd3e3;
    --label-blue-deep: #9cc7d9;
    --silver-light: #e9ecef;
    --silver-dark: #8e959b;
    --brand-red: #7e1518;
    --title-red: #9a1f22;
    --ink-dark: #2a2a2a;
    --ink-body: #4b5257;
    --dash: #3a3a3a;
    --white: #ffffff;
  }
  * { box-sizing: border-box; margin: 0; padding: 0; }
  html, body {
    width: 1200px; height: 912px; overflow: hidden;
    background: var(--backdrop);
  }
  .label {
    position: absolute; left: 50px; top: 276px;
    width: 1100px; height: 360px;
    background: linear-gradient(180deg, var(--label-blue) 0%, var(--label-blue-deep) 100%);
    overflow: hidden;
  }
  .label__edge {
    position: absolute; left: 0; right: 0; height: 12px;
    background: linear-gradient(180deg, var(--silver-light), var(--silver-dark), var(--silver-light));
  }
  .label__edge--top { top: 0; }
  .label__edge--bottom { bottom: 0; }

  .credits {
    position: absolute; left: 28px; top: 40px; height: 280px;
    writing-mode: vertical-rl;
    font-family: "Arimo", Arial, sans-serif;
    font-size: 16px; line-height: 20px; color: var(--ink-dark);
  }
  .natural-tag {
    position: absolute; left: 140px; top: 152px;
    width: 30px; height: 130px;
    background: var(--brand-red); border-radius: 3px;
    display: flex; align-items: center; justify-content: center;
  }
  .natural-tag span {
    writing-mode: vertical-rl; transform: rotate(180deg);
    font-family: "Arimo", Arial, sans-serif; font-weight: 700;
    font-size: 14px; color: var(--white); letter-spacing: 0.5px;
  }
  .frame-lines { position: absolute; inset: 0; }

  .fly-art {
    position: absolute; border-radius: 50%;
    background: radial-gradient(circle, rgba(60,60,60,0.45), rgba(60,60,60,0.12) 70%, transparent 72%);
  }
  .fly-art--small { left: 270px; top: 40px; width: 60px; height: 60px; }
  .fly-art--large { left: 868px; top: 90px; width: 90px; height: 90px; }

  .brand {
    position: absolute; left: 400px; top: 34px;
    width: 316px; height: 70px;
    display: flex; align-items: center; justify-content: center; gap: 12px;
  }
  .brand__mark {
    width: 14px; height: 14px; background: var(--brand-red);
  }
  .brand__name {
    font-family: "Arimo", Arial, sans-serif; font-weight: 700;
    font-size: 42px; color: var(--brand-red); line-height: 1;
  }
  .product-title {
    position: absolute; left: 190px; top: 120px; width: 690px;
    font-family: "Kalam", cursive; font-weight: 700;
    font-size: 50px; line-height: 1; color: var(--title-red);
    text-align: center; white-space: nowrap;
  }
  .product-subtitle {
    position: absolute; left: 206px; top: 176px; width: 650px;
    font-family: "Kalam", cursive; font-weight: 700;
    font-size: 30px; line-height: 1; color: var(--ink-dark);
    padding-bottom: 4px; border-bottom: 2px solid var(--title-red);
    text-align: center;
  }
  .ingredients {
    position: absolute; left: 198px; top: 224px; width: 540px;
    font-family: "Arimo", Arial, sans-serif;
    font-size: 19px; line-height: 23px; color: var(--ink-body);
  }
  .origin {
    position: absolute; left: 826px; top: 252px;
    display: flex; flex-direction: column; align-items: center;
  }
  .origin__badge {
    width: 66px; height: 40px; border-radius: 4px;
    background: var(--white);
  }
  .origin__text {
    margin-top: 4px;
    font-family: "Arimo", Arial, sans-serif; font-size: 11px; color: var(--ink-dark);
  }
</style>
</head>
<body>
  <section class="label" aria-label="Jar label">
    <div class="label__edge label__edge--top"></div>
    <div class="label__edge label__edge--bottom"></div>

    <p class="credits">Formulated by:<br>Australian Pharmacists<br>Carla Whitby and Rob Kettering<br>Phone - 0413862207</p>

    <svg class="frame-lines" width="1100" height="360" viewBox="0 0 1100 360" aria-hidden="true">
      <path d="M155 152 L155 70 Q155 62 163 62 L275 62" fill="none" stroke="var(--dash)" stroke-width="2" stroke-dasharray="7 5"/>
      <path d="M155 282 L155 315 Q155 323 163 323 L820 323" fill="none" stroke="var(--dash)" stroke-width="2" stroke-dasharray="7 5"/>
      <path d="M910 182 Q960 220 910 250 Q880 268 900 290" fill="none" stroke="var(--dash)" stroke-width="2" stroke-dasharray="7 5"/>
    </svg>

    <div class="natural-tag"><span>100% Natural</span></div>

    <div class="fly-art fly-art--small" role="img" aria-label="Small line drawing of a sandfly"></div>
    <div class="fly-art fly-art--large" role="img" aria-label="Line drawing of a sandfly in flight"></div>

    <div class="brand"><span class="brand__mark" aria-hidden="true"></span><span class="brand__name">Rob &amp; Jo’s</span></div>

    <h1 class="product-title">Goodbye to Midge bites</h1>
    <h2 class="product-subtitle">Natural Sandfly Repellent</h2>

    <p class="ingredients">Contains Essential Oils of cedar wood, rosemary, cinnamon, citronella, lavender, eucalyptus and clove in a moisturising base.</p>

    <div class="origin">
      <div class="origin__badge" role="img" aria-label="Australian flag badge"></div>
      <span class="origin__text">Made in Australia</span>
    </div>
  </section>
</body>
</html>
```